Modern Website Design for an Online Travel Agency.. Design Only!!

Hi there!

We are building an website for our travel agency that caters to tourists traveling to the Cayman Islands. We provide travel information and take bookings for various tours available here.

We need designs for 8 different web page layouts. You can see the layout specifications in two attached documents. We do not have a need for the coding to be done. This will simply act as a blueprint for our developer to build from.

The important pages are the 'Home Page' 'checkout page' and the ‘Checkout Page’ (Page 1 & 10 in the PDF ‘Website Layout’)

The MOST important page is ‘Tour Search Page’ (page 6)

If you intend on only submitting one page design, please submit a design for page 6. Be aware though, the more of these 3 page designs you submit, the more likely we are to move forward with you!

At this stage, we are simply looking to develop the most aesthetic website design layout possible.

- The website should be colour coordinated with the logo. You can most certainly use other colours if you feel they complement the overall design of the website well.

- Everything must be laid out in an EXTREMELY simple & ‘easy to navigate’ way. The key is simplicity & Functionality. There is no need for messy or elaborate graphics.

- The website MUST have a VERY clean and modern appearance.

- We want the main background to be white, but you can use light grey in places to compliment or add dimension if you feel necessary.

- We will appreciate a good use of shadows and especially a good use of icons. (You can see examples of icons we have already designed, we are definitely open to new icon design concepts too)

- We will reward imagination and original thinking! Essentially we want a website with a creative touch and unique design elements, whilst maintaining that clean and simple layout.

- Most importantly!! - Paying attention to the small details will be highly rewarded (A well balanced and seamless use of fonts, colours, dimensions, shadowing, positioning, etc)

If you have any questions, please don’t hesitate to ask.

We’re excited to see your design submissions!

Thank you!!

You can find all the support documents and content at: https://www.filevorra.net/sh/9qm2rtwplexan7c/QQBmTtZnPdLsWEGxvvaJpLmRw?dl=0

Target Market(s)

Tourists

Industry/Entity Type

Travel

Number of Pages Required

5+ page

Font styles to use
Sans Serif

Colors

Designer to choose colors to be used in the design.

Requirements
Must have
• Must be very clean and modern.
• Must be simple and bold
• Must be color coordinated in a way that makes sense
• White background
Nice to have
• Good use of shadows and Icons
Should not have
• Over use of messy graphics
• And design layout which is not right angled (using anything but vertical or horizontal for the edges in the design)

```html
<!DOCTYPE html>
<html lang="en">
<head>
<meta charset="utf-8">
<title>IsleRoute – Outdoor Activities</title>
<link rel="stylesheet" href="https://fonts.googleapis.com/css2?family=Montserrat:wght@400;500;600;700;800&display=swap">
<style>
:root{
  --green:#9aca3c;
  --blue:#0a6cd5;
  --ink:#1d1d1f;
  --text:#3c3c3c;
  --muted:#8a8a8a;
  --line:#e3e3e3;
  --gold:#f2b705;
  --white:#ffffff;
}
*{box-sizing:border-box;margin:0;padding:0}
html,body{width:681px;height:1200px;overflow:hidden;background:var(--white)}
body{font-family:"Montserrat",sans-serif;color:var(--text)}
.page{position:relative;width:681px;height:1200px;overflow:hidden}
.abs{position:absolute}

/* top bar */
.topbar{left:0;top:0;width:681px;height:18px;background:var(--green)}
.topbar .social{position:absolute;left:68px;top:6px;display:flex;gap:9px}
.topbar .social span{width:6px;height:6px;border-radius:50%;background:var(--white)}
.topbar .util{position:absolute;right:62px;top:5px;display:flex;gap:16px;font-size:5.5px;font-weight:600;color:var(--white)}

/* header */
.brand{left:62px;top:38px;display:flex;align-items:center;gap:5px}
.brand-mark{width:16px;height:16px;background:var(--green)}
.brand-name{font-size:17px;font-weight:700;color:var(--blue)}
.btn-dest{left:524px;top:37px;width:94px;height:21px;background:var(--blue);color:var(--white);font-size:6.5px;font-weight:700;display:flex;align-items:center;justify-content:center;gap:4px}

/* nav */
.nav{left:0;top:74px;width:681px;height:32px;background:var(--green)}
.nav a{position:absolute;top:0;height:32px;display:flex;align-items:center;justify-content:center;color:var(--white);font-size:7.6px;font-weight:800;text-decoration:none;border-left:1px solid rgba(255,255,255,.45)}
.nav a.last{border-right:1px solid rgba(255,255,255,.45)}

/* sidebar */
.map{left:59px;top:126px;width:164px;height:115px;background:linear-gradient(120deg,#6aa9e6 0%,#8cc0ee 55%,#e9e9e6 56%,#efefec 100%)}
.filters{left:60px;top:254px;width:163px;height:566px;border:1px solid var(--line);background:var(--white)}
.filters-head{height:39px;background:var(--green);color:var(--white);font-size:13px;font-weight:800;padding:12px 0 0 20px}
.f-title{position:absolute;left:20px;font-size:8.5px;font-weight:700;color:var(--ink)}
.f-item{position:absolute;left:20px;font-size:6.6px;font-weight:500;color:var(--text)}
.f-rule{position:absolute;left:0;width:161px;height:1px;background:var(--line)}
.slider{position:absolute;left:23px;width:110px;height:1px;background:var(--blue)}
.slider::before,.slider::after{content:"";position:absolute;top:-3px;width:6px;height:6px;border-radius:50%;background:var(--white);border:1px solid #cfcfcf;box-shadow:0 1px 2px rgba(0,0,0,.15)}
.slider::before{left:-3px}.slider::after{right:-3px}
.s-lab{position:absolute;font-size:4.4px;color:var(--ink)}
.check{position:absolute;left:14px;font-size:6.6px;font-weight:500;color:var(--text);padding-left:0}
.check::before{content:"";position:absolute;left:-8px;top:1px;width:5px;height:5px;border:1px solid #e0e0e0;background:#fafafa}

/* search */
.search{left:242px;top:126px;width:218px;height:22px;border:1px solid var(--line);font-size:6.6px;color:var(--muted);display:flex;align-items:center;padding-left:9px;gap:4px}
.sort-lab{left:467px;top:126px;width:48px;height:22px;background:var(--blue);color:var(--white);font-size:6.4px;font-weight:700;display:flex;align-items:center;justify-content:center}
.sort-val{left:515px;top:126px;width:88px;height:22px;border:1px solid var(--line);font-size:6.4px;color:#b5b5b5;display:flex;align-items:center;justify-content:center}
.results-title{left:242px;top:159px;font-size:12px;font-weight:700;color:var(--ink)}
.results-count{left:242px;top:175px;font-size:6.6px;font-weight:500;color:var(--ink)}

/* activity card */
.card{position:absolute;width:168px;height:194px;background:var(--white);box-shadow:0 1px 4px rgba(0,0,0,.12)}
.card-photo{position:absolute;left:0;top:0;width:168px;height:97px}
.tag{position:absolute;left:-5px;top:5px;width:78px;height:16px;background:var(--blue);color:var(--white);font-size:6.8px;font-weight:700;display:flex;align-items:center;justify-content:center}
.badge{position:absolute;left:7px;top:77px;width:33px;height:24px;background:var(--green);color:var(--white);font-size:6.3px;font-weight:800;line-height:8px;text-align:center;padding-top:4px}
.price{position:absolute;left:79px;top:87px;width:92px;height:16px;background:var(--blue);color:var(--white);font-size:6.6px;font-weight:700;display:flex;align-items:center;justify-content:center;gap:1px}
.price b{font-size:8.5px;font-weight:800}
.card-title{position:absolute;left:9px;top:108px;width:155px;font-size:7.6px;font-weight:800;line-height:8.6px;color:var(--ink)}
.rating{position:absolute;left:9px;top:129px;display:flex;align-items:center;gap:3px}
.rating .stars{font-size:8px;color:var(--gold);letter-spacing:-1px}
.rating small{font-size:4.6px;color:var(--text)}
.meta{position:absolute;left:13px;display:flex;align-items:center;gap:3px;font-size:5.6px;font-weight:500;color:var(--ink)}
.meta svg{width:5px;height:5px}
.organizer{position:absolute;left:0;top:170px;width:168px;height:24px;background:var(--green);color:var(--white);font-size:6.8px;font-weight:600;display:flex;align-items:center;justify-content:center}
.card--outline .organizer{background:var(--white);color:#555;border-top:1px solid var(--green)}

/* steps */
.steps{left:58px;top:838px;width:566px;height:181px;border:1px solid var(--green)}
.step{position:absolute;top:0;width:130px}
.step-num{position:absolute;width:17px;height:17px;border-radius:50%;background:#eef2fa;color:var(--blue);font-size:7.5px;display:flex;align-items:center;justify-content:center}
.step-text{position:absolute;font-size:7px;line-height:7.4px;color:var(--blue);font-family:"Montserrat",sans-serif;font-weight:400}
.step-art{position:absolute;width:112px;height:106px;border-radius:6px}

/* footer */
.f-col{position:absolute;top:1050px}
.f-col h4{font-size:8.5px;font-weight:700;color:var(--green);margin-bottom:8px}
.f-col a{display:block;font-size:6.8px;color:#8d8d8d;text-decoration:none;height:14.2px}
.f-rule-bottom{left:82px;top:1146px;width:517px;height:1px;background:var(--line)}
.copyright{left:86px;top:1166px;font-size:6.8px;color:#8d8d8d}
.f-social{left:537px;top:1164px;display:flex;gap:9px}
.f-social span{width:10px;height:10px;border-radius:50%;background:var(--green)}
</style>
</head>
<body>
<div class="page">

  <div class="abs topbar">
    <div class="social"><span></span><span></span><span></span><span></span></div>
    <div class="util"><span>EN ⌄</span><span>USD$</span><span>LOGIN</span></div>
  </div>

  <div class="abs brand"><span class="brand-mark"></span><span class="brand-name">IsleRoute</span></div>
  <div class="abs btn-dest">
    <svg width="6" height="7" viewBox="0 0 10 12"><path d="M5 1a4 4 0 0 0-4 4c0 3 4 6.5 4 6.5S9 8 9 5a4 4 0 0 0-4-4z" fill="none" stroke="#fff" stroke-width="1.3"/></svg>
    DESTINATIONS ⌄
  </div>

  <nav class="abs nav">
    <a style="left:57px;width:134px">DISCOVER CAYMAN</a>
    <a style="left:191px;width:113px">THING TO DO</a>
    <a style="left:304px;width:136px">MY TRIP PLANNER</a>
    <a style="left:440px;width:80px">MAP</a>
    <a class="last" style="left:520px;width:104px">CONTACT US</a>
  </nav>

  <div class="abs map" role="img" aria-label="Map of the islands and surrounding sea"></div>

  <aside class="abs filters">
    <div class="filters-head">Filters:</div>
    <div class="f-title" style="top:52px">Location</div>
    <div class="f-item" style="top:68px">- Grand Cayman</div>
    <div class="f-item" style="top:80px">- Cayman Brac</div>
    <div class="f-rule" style="top:95px"></div>

    <div class="f-title" style="top:112px">Price Range</div>
    <div class="slider" style="top:126px"></div>
    <div class="s-lab" style="left:20px;top:132px">$10</div>
    <div class="s-lab" style="left:124px;top:132px">$1000</div>

    <div class="f-title" style="top:155px">Duration</div>
    <div class="slider" style="top:167px"></div>
    <div class="s-lab" style="left:20px;top:173px">0 hours</div>
    <div class="s-lab" style="left:124px;top:173px">3 days</div>

    <div class="f-title" style="top:197px">People in your Group</div>
    <div class="slider" style="top:209px"></div>
    <div class="s-lab" style="left:20px;top:215px">0 hours</div>
    <div class="s-lab" style="left:124px;top:215px">3 days</div>
    <div class="f-rule" style="top:239px"></div>

    <div class="f-title" style="top:254px">Activities</div>
    <div class="check" style="left:28px;top:271px">Kiteboarding</div>
    <div class="check" style="left:28px;top:285px">Museums</div>
    <div class="check" style="left:28px;top:299px">Boat Trips</div>
    <div class="check" style="left:28px;top:313px">Scuba diving</div>
    <div class="check" style="left:28px;top:328px">Deep-Sea Fishing</div>
    <div class="check" style="left:28px;top:342px">Snorkelling</div>
    <div class="check" style="left:28px;top:356px">Kiteboarding</div>
    <div class="check" style="left:28px;top:370px">Museums</div>
    <div class="check" style="left:28px;top:384px">Boat Trips</div>
    <div class="check" style="left:28px;top:399px">Scuba diving</div>
    <div class="check" style="left:28px;top:413px">Deep-Sea Fishing</div>
    <div class="check" style="left:28px;top:427px">Snorkelling</div>
    <div class="check" style="left:28px;top:441px">Kiteboarding</div>
    <div class="check" style="left:28px;top:455px">Museums</div>
    <div class="check" style="left:28px;top:470px">Boat Trips</div>
    <div class="check" style="left:28px;top:484px">Scuba diving</div>

    <div class="f-title" style="top:508px">Other Filters</div>
    <div class="check" style="left:28px;top:526px">Fitness Level</div>
    <div class="check" style="left:28px;top:540px">Family</div>
  </aside>

  <div class="abs search">
    <svg width="6" height="7" viewBox="0 0 10 12"><path d="M5 1a4 4 0 0 0-4 4c0 3 4 6.5 4 6.5S9 8 9 5a4 4 0 0 0-4-4z" fill="none" stroke="#9a9a9a" stroke-width="1.1"/></svg>
    YOUR LOCATION
  </div>
  <div class="abs sort-lab">SORT BY:</div>
  <div class="abs sort-val">POPULARITY ⌄</div>

  <h1 class="abs results-title">OUR TOTAL OUTDOOR ACTIVITIES</h1>
  <p class="abs results-count">2087 activities match your criteria</p>

  <!-- row 1 -->
  <article class="card card--outline" style="left:244px;top:196px">
    <div class="card-photo" role="img" aria-label="Divers swimming over a coral reef" style="background:linear-gradient(180deg,#35b9c9,#1f8fa6 60%,#5c6b4a)"></div>
    <div class="tag">Scuba Diving</div><div class="badge">TOP<br>RATED</div>
    <div class="price">From <b>$9099/</b> person</div>
    <h2 class="card-title">SCUBA DIVING IN GRAND CAYMAN, THE LARGEST ISLAND</h2>
    <div class="rating"><span class="stars">★★★★★</span><small>100 Reviews</small></div>
    <div class="meta" style="top:145px"><svg viewBox="0 0 10 12"><path d="M5 1a4 4 0 0 0-4 4c0 3 4 6.5 4 6.5S9 8 9 5a4 4 0 0 0-4-4z" fill="none" stroke="#555" stroke-width="1.2"/></svg>Western Caribbean Sea</div>
    <div class="meta" style="top:154px"><svg viewBox="0 0 10 10"><circle cx="5" cy="5" r="4" fill="none" stroke="#555" stroke-width="1.2"/><path d="M5 3v2.3h1.8" fill="none" stroke="#555"/></svg>Full Day</div>
    <div class="organizer">Organized by Lorem ipsum dolor</div>
  </article>

  <article class="card" style="left:435px;top:196px">
    <div class="card-photo" role="img" aria-label="Aerial view of an island coastline" style="background:linear-gradient(170deg,#3a6aa8,#2a78b8 45%,#7fa08a 60%,#3d86c2)"></div>
    <div class="tag">Scuba Diving</div><div class="badge">TOP<br>RATED</div>
    <div class="price">From <b>$9099/</b> person</div>
    <h2 class="card-title">SCUBA DIVING IN GRAND CAYMAN, THE LARGEST ISLAND</h2>
    <div class="rating"><span class="stars">★★★★★</span><small>100 Reviews</small></div>
    <div class="meta" style="top:145px"><svg viewBox="0 0 10 12"><path d="M5 1a4 4 0 0 0-4 4c0 3 4 6.5 4 6.5S9 8 9 5a4 4 0 0 0-4-4z" fill="none" stroke="#555" stroke-width="1.2"/></svg>Western Caribbean Sea</div>
    <div class="meta" style="top:154px"><svg viewBox="0 0 10 10"><circle cx="5" cy="5" r="4" fill="none" stroke="#555" stroke-width="1.2"/><path d="M5 3v2.3h1.8" fill="none" stroke="#555"/></svg>Full Day</div>
    <div class="organizer">Organized by Lorem ipsum dolor</div>
  </article>

  <!-- row 2 -->
  <article class="card" style="left:244px;top:408px">
    <div class="card-photo" role="img" aria-label="Turquoise lagoon with a green shoreline" style="background:linear-gradient(180deg,#4aa7dc,#6f9a57 30%,#58d2d2 45%,#2fbfc6)"></div>
    <div class="tag">Scuba Diving</div><div class="badge">TOP<br>RATED</div>
    <div class="price">From <b>$9099/</b> person</div>
    <h2 class="card-title">SCUBA DIVING IN GRAND CAYMAN, THE LARGEST ISLAND</h2>
    <div class="rating"><span class="stars">★★★★★</span><small>100 Reviews</small></div>
    <div class="meta" style="top:145px"><svg viewBox="0 0 10 12"><path d="M5 1a4 4 0 0 0-4 4c0 3 4 6.5 4 6.5S9 8 9 5a4 4 0 0 0-4-4z" fill="none" stroke="#555" stroke-width="1.2"/></svg>Western Caribbean Sea</div>
    <div class="meta" style="top:154px"><svg viewBox="0 0 10 10"><circle cx="5" cy="5" r="4" fill="none" stroke="#555" stroke-width="1.2"/><path d="M5 3v2.3h1.8" fill="none" stroke="#555"/></svg>Full Day</div>
    <div class="organizer">Organized by Lorem ipsum dolor</div>
  </article>

  <article class="card" style="left:435px;top:408px">
    <div class="card-photo" role="img" aria-label="Group of friends jumping on a beach" style="background:linear-gradient(180deg,#2d6fc4,#5b8fd0 45%,#b88a72 70%,#d9cfb6)"></div>
    <div class="tag">Scuba Diving</div><div class="badge">TOP<br>RATED</div>
    <div class="price">From <b>$9099/</b> person</div>
    <h2 class="card-title">SCUBA DIVING IN GRAND CAYMAN, THE LARGEST ISLAND</h2>
    <div class="rating"><span class="stars">★★★★★</span><small>100 Reviews</small></div>
    <div class="meta" style="top:145px"><svg viewBox="0 0 10 12"><path d="M5 1a4 4 0 0 0-4 4c0 3 4 6.5 4 6.5S9 8 9 5a4 4 0 0 0-4-4z" fill="none" stroke="#555" stroke-width="1.2"/></svg>Western Caribbean Sea</div>
    <div class="meta" style="top:154px"><svg viewBox="0 0 10 10"><circle cx="5" cy="5" r="4" fill="none" stroke="#555" stroke-width="1.2"/><path d="M5 3v2.3h1.8" fill="none" stroke="#555"/></svg>Full Day</div>
    <div class="organizer">Organized by Lorem ipsum dolor</div>
  </article>

  <!-- row 3 -->
  <article class="card" style="left:244px;top:621px">
    <div class="card-photo" role="img" aria-label="Person relaxing on a float at sea under a cloudy sky" style="background:linear-gradient(180deg,#9fb7d6,#d8dfe8 40%,#6f8ea8 65%,#4d6d86)"></div>
    <div class="tag">Scuba Diving</div><div class="badge">TOP<br>RATED</div>
    <div class="price">From <b>$9099/</b> person</div>
    <h2 class="card-title">SCUBA DIVING IN GRAND CAYMAN, THE LARGEST ISLAND</h2>
    <div class="rating"><span class="stars">★★★★★</span><small>100 Reviews</small></div>
    <div class="meta" style="top:145px"><svg viewBox="0 0 10 12"><path d="M5 1a4 4 0 0 0-4 4c0 3 4 6.5 4 6.5S9 8 9 5a4 4 0 0 0-4-4z" fill="none" stroke="#555" stroke-width="1.2"/></svg>Western Caribbean Sea</div>
    <div class="meta" style="top:154px"><svg viewBox="0 0 10 10"><circle cx="5" cy="5" r="4" fill="none" stroke="#555" stroke-width="1.2"/><path d="M5 3v2.3h1.8" fill="none" stroke="#555"/></svg>Full Day</div>
    <div class="organizer">Organized by Lorem ipsum dolor</div>
  </article>

  <article class="card" style="left:435px;top:621px">
    <div class="card-photo" role="img" aria-label="Snorkeller swimming beside a stingray" style="background:linear-gradient(180deg,#5fb7c4,#7fc3c4 50%,#b7c2ae)"></div>
    <div class="tag">Scuba Diving</div><div class="badge">TOP<br>RATED</div>
    <div class="price">From <b>$9099/</b> person</div>
    <h2 class="card-title">SCUBA DIVING IN GRAND CAYMAN, THE LARGEST ISLAND</h2>
    <div class="rating"><span class="stars">★★★★★</span><small>100 Reviews</small></div>
    <div class="meta" style="top:145px"><svg viewBox="0 0 10 12"><path d="M5 1a4 4 0 0 0-4 4c0 3 4 6.5 4 6.5S9 8 9 5a4 4 0 0 0-4-4z" fill="none" stroke="#555" stroke-width="1.2"/></svg>Western Caribbean Sea</div>
    <div class="meta" style="top:154px"><svg viewBox="0 0 10 10"><circle cx="5" cy="5" r="4" fill="none" stroke="#555" stroke-width="1.2"/><path d="M5 3v2.3h1.8" fill="none" stroke="#555"/></svg>Full Day</div>
    <div class="organizer">Organized by Lorem ipsum dolor</div>
  </article>

  <!-- how it works -->
  <section class="abs steps">
    <div class="step-num" style="left:4px;top:25px">1.</div>
    <div class="step-text" style="left:6px;top:45px">Choose Your<br>Favorite Activities</div>
    <div class="step-art" role="img" aria-label="Illustration of a traveller choosing activities" style="left:12px;top:62px;background:linear-gradient(160deg,#eaf3fb,#dff0d2)"></div>

    <div class="step-num" style="left:142px;top:23px">2.</div>
    <div class="step-text" style="left:144px;top:43px">Use Our Online<br>Travel Planner</div>
    <div class="step-art" role="img" aria-label="Illustration of a traveller using an online planner" style="left:148px;top:62px;background:linear-gradient(160deg,#eaf3fb,#e4f2d4)"></div>

    <div class="step-num" style="left:287px;top:23px">3.</div>
    <div class="step-text" style="left:289px;top:43px">We Make All<br>The Arrangements</div>
    <div class="step-art" role="img" aria-label="Illustration of travel arrangements being made" style="left:288px;top:62px;background:linear-gradient(160deg,#eef3f3,#e6f3d2)"></div>

    <div class="step-num" style="left:432px;top:23px">4.</div>
    <div class="step-text" style="left:434px;top:43px">Relax and Enjoy<br>Your Vacation</div>
    <div class="step-art" role="img" aria-label="Illustration of people relaxing on a beach" style="left:440px;top:62px;background:linear-gradient(160deg,#eef4ee,#dff1ee)"></div>
  </section>

  <!-- footer -->
  <div class="f-col" style="left:86px"><h4>COMPANY</h4><a>About us</a><a>How it works?</a><a>Our investers</a><a>Contact us</a><a>Work with us</a></div>
  <div class="f-col" style="left:247px"><h4>SUPPORT</h4><a>FAQ</a><a>Legal notices</a><a>Cancellation policy</a><a>Terms of use</a><a>Privacy policy</a></div>
  <div class="f-col" style="left:398px"><h4>FOLLOW US</h4><a>Press room</a><a>Our ambassadors</a><a>Magazine</a></div>
  <div class="f-col" style="left:530px"><h4>PARTNERS</h4><a>Offer your activities</a><a>Become an affiliate</a></div>

  <div class="abs f-rule-bottom"></div>
  <p class="abs copyright">Copyright © 2019 Company name. All rights reserved.</p>
  <div class="abs f-social"><span></span><span></span><span></span><span></span></div>

</div>
</body>
</html>
```